Redesign of business card for Silverbrook Mechanical

We are looking for a new design for our business cards for Silverbrook Mechanical. We are a plumbing & HVAC construction company, operating on the West Coast of Canada and USA. Logo attached.
Industry/Entity Type
Construction - Plumbing & HVAC
Contact Information for Business Card
Name, address, phone numbers, email, website address
Look and feel

```html
<!DOCTYPE html>
<html lang="en">
<head>
<meta charset="utf-8">
<title>Silverbrook Mechanical – Business Card Options</title>
<link rel="stylesheet" href="https://fonts.googleapis.com/css2?family=Arimo:wght@700&family=Montserrat:wght@400;500;600;700&display=swap">
<style>
  :root {
    --stage: #c6c6c6;
    --ink: #111111;
    --ink-soft: #1c1c1c;
    --grey-text: #6f6f6f;
    --grey-band: #999999;
    --rule: #7a7a7a;
    --paper: #ffffff;
    --back-dark: #151515;
    --back-mid: #4a4b4b;
    --back-type: #8a8a8a;
  }
  * { box-sizing: border-box; margin: 0; padding: 0; }
  html, body { width: 1200px; height: 1166px; overflow: hidden; }
  body {
    background: var(--stage);
    position: relative;
    font-family: "Montserrat", sans-serif;
    color: var(--ink);
  }
  .option-title {
    position: absolute;
    left: 0; width: 1200px;
    text-align: center;
    font-family: "Arimo", sans-serif;
    font-weight: 700;
    font-size: 50px;
    letter-spacing: 0.5px;
    color: #000;
    line-height: 1;
  }
  .option-title.square { top: 124px; }
  .option-title.rounded { top: 594px; }

  .card {
    position: absolute;
    width: 523px;
    height: 299px;
    overflow: hidden;
    box-shadow: 2px 3px 5px rgba(0,0,0,0.35);
  }
  .card.is-rounded { border-radius: 37px; }
  .row-square .card { top: 221px; }
  .row-rounded .card { top: 693px; }
  .card.front { left: 59px; background: var(--paper); }
  .card.back {
    left: 618px;
    background: linear-gradient(115deg, var(--back-dark) 0%, #0c0c0c 38%, #1e1e1e 55%, var(--back-mid) 78%, #2a2a2a 100%);
  }

  .brand {
    position: absolute;
    right: 35px;
    top: 62px;
    display: flex;
    align-items: center;
    gap: 8px;
    font-weight: 700;
    font-size: 17px;
    letter-spacing: 0.6px;
    color: var(--ink-soft);
  }
  .brand-square { width: 12px; height: 12px; background: var(--ink-soft); }

  .person-name {
    position: absolute;
    left: 34px; top: 160px;
    font-weight: 700;
    font-size: 17px;
    letter-spacing: 0.4px;
    color: var(--ink-soft);
  }
  .person-name .surname { color: var(--grey-text); }
  .person-role {
    position: absolute;
    left: 34px; top: 181px;
    font-size: 13.5px;
    font-weight: 500;
    color: var(--ink-soft);
  }
  .rule {
    position: absolute;
    left: 34px; right: 34px; top: 202px;
    height: 1px;
    background: var(--rule);
  }
  .contact-list {
    position: absolute;
    left: 34px; top: 214px;
    list-style: none;
    font-size: 13.5px;
    color: var(--grey-text);
    line-height: 17.6px;
  }
  .contact-list li { display: flex; align-items: center; gap: 5px; }
  .contact-list svg { width: 11px; height: 11px; fill: var(--ink-soft); flex: none; }
  .contact-list .em { color: var(--ink-soft); }
  .address {
    position: absolute;
    right: 35px; top: 231px;
    text-align: right;
    font-size: 13.5px;
    color: var(--grey-text);
    line-height: 17.6px;
  }
  .footer-band { position: absolute; left: 0; bottom: 0; width: 523px; height: 11px; }

  .back-name {
    position: absolute;
    left: 0; right: 0; top: 134px;
    text-align: center;
    font-weight: 600;
    font-size: 25px;
    letter-spacing: 1px;
    color: var(--back-type);
  }
</style>
</head>
<body>

<h2 class="option-title square">SQUARE CORNERS</h2>
<section class="row-square">
  <article class="card front">
    <div class="brand"><span class="brand-square"></span>SILVERBROOK MECHANICAL</div>
    <div class="person-name">JONATHAN <span class="surname">SMITH</span></div>
    <div class="person-role">Manager</div>
    <div class="rule"></div>
    <ul class="contact-list">
      <li><svg viewBox="0 0 12 12"><path d="M1 4c0-2 2-2.5 5-2.5S11 2 11 4H8.5V3h-5v1zM2.5 5h7l1.5 5.5H1z"/></svg>123-456-2100</li>
      <li><svg viewBox="0 0 12 12"><path d="M1 5l5-4 5 4v6H1zm1 .6V10h8V5.6L6 8.5z"/></svg>youremail@mailbox.com</li>
      <li><svg viewBox="0 0 12 12"><circle cx="6" cy="6" r="5.5"/></svg>www.<span class="em">yourwebsite</span>.com</li>
    </ul>
    <div class="address">Your address, city<br>state, ZIP 0000</div>
    <svg class="footer-band" viewBox="0 0 523 11" preserveAspectRatio="none">
      <polygon points="0,0 365,0 355,11 0,11" fill="var(--ink-soft)"/>
      <polygon points="374,0 523,0 523,11 364,11" fill="var(--grey-band)"/>
    </svg>
  </article>
  <article class="card back">
    <div class="back-name">SILVERBROOK MECHANICAL</div>
  </article>
</section>

<h2 class="option-title rounded">ROUNDED CORNERS</h2>
<section class="row-rounded">
  <article class="card front is-rounded">
    <div class="brand"><span class="brand-square"></span>SILVERBROOK MECHANICAL</div>
    <div class="person-name">JONATHAN <span class="surname">SMITH</span></div>
    <div class="person-role">Manager</div>
    <div class="rule"></div>
    <ul class="contact-list">
      <li><svg viewBox="0 0 12 12"><path d="M1 4c0-2 2-2.5 5-2.5S11 2 11 4H8.5V3h-5v1zM2.5 5h7l1.5 5.5H1z"/></svg>123-456-2100</li>
      <li><svg viewBox="0 0 12 12"><path d="M1 5l5-4 5 4v6H1zm1 .6V10h8V5.6L6 8.5z"/></svg>youremail@mailbox.com</li>
      <li><svg viewBox="0 0 12 12"><circle cx="6" cy="6" r="5.5"/></svg>www.<span class="em">yourwebsite</span>.com</li>
    </ul>
    <div class="address">Your address, city<br>state, ZIP 0000</div>
    <svg class="footer-band" viewBox="0 0 523 11" preserveAspectRatio="none">
      <polygon points="0,0 365,0 355,11 0,11" fill="var(--ink-soft)"/>
      <polygon points="374,0 523,0 523,11 364,11" fill="var(--grey-band)"/>
    </svg>
  </article>
  <article class="card back is-rounded">
    <div class="back-name">SILVERBROOK MECHANICAL</div>
  </article>
</section>

</body>
</html>
```